Brackenridge Fish House Menu design

We are a new Seafood Restaurant in NW Montana. We will be the only one in about 200 Miles. We are a Casual/Upscale Restaurant featureing and Oyster Bar/Live Lobster Tank/ Outdoor Seating with beautiful lake views. We have huge garage doors that open up to our big outdoor patio and outdor stage for live music.
I'm interested in having our menu having the ability to add a printed page daily or weekly showing the fresh fish and Oysters that we have as well as specials which will also be represented on the chalk board.
We have 75 Bottle wine list divided by grape variatal such as: Chardonnay, Savagnion Blanc, Reisling, Champagne, Pinot Noir, Melot, Syrah, Cabernet Sauvignon, Interesting Whites and Interesting reds.
We are designing the restaurant to look more Contemporary/urban chic/industrial with reclaimed wood as well. White's Blues and Grey's are the prevolent colors.
I also have a logo we can send over.

Target Market(s)

30-65 age mainly caucasian from the Northwest region as well as tons of Canadians.

Industry/Entity Type

Restaurant

Requirements
Must have
• "Eat the Fish" is our Tagline
American and Canadian flags that are crossed
Family owned and operated

Disclaimer: All steaks and Burgers are cooked to order. "Consuming raw, undercooked and unpasteurized food items may increase your chance of foodborne illnesses." We use nut and nut based oils in some of our menu items. If you are allergic to nuts or any other foods, please let us know.

Also here is the menu: Feel free to use whatever subcatagory heading you choose this was just for us.
FINAL MENU

SMALL PLATES
1. Sweet Thai Chili Calamari
2. Shrimp Stuffed Jalapeños
3. Hamachi Crudo
4. House Smoked Salmon with Tandem Crackers and Pickled Celery
5. Seared Teriyaki Tidbits
6. Sliders
• Crab Salad
• Sausage with Caramelized Onions, Peppers and Provolone
• Mini Cheeseburgers
7. Fried Green Tomatoes with Crab and Tarragon-Chive Aioli
8. Tomato Soup
9. Seafood Bisque
10. House Salad with Choice of Dressings
11. Small Caesar Salad

FARM
1. Caesar Salad Entrees
• Chicken
• Fish
• Crab
2. Seafood Cobb
3. Caprese
4. Farmhouse

SNACKS
1. Fish Tacos
2. Rolls
• Lobster
• Crab
• Shrimp
3. Grilled Chicken Avocado and Bacon
4. Grilled Cheese with Tomato Soup

OCEANS
1. Wood Grilled Black Smoked Sea Salt and Pepper Salmon
2. Miso Black Cod
3. Vela Rino White Fish
4. Whole Fish
5. Fish n Chips
6. Lobster
7. Steamed Clams and/or Mussels
8. Seared Scallops
9. Roasted Garlic Shrimp
10. Crab Cakes with Trio of Dipping Butters

RANCH
1. Wood Grilled 16 oz Rib Eye
2. Wood Grilled 10 oz Top Sirloin
3. Wood Grilled Half Chicken
4. Wood Grilled Pork Chop

SWEETS
1. Key Lime Pie
2. Molted Chocolate Cake
3. Banana Fosters / Cherries Jubilee

Nice to have
• We have a little bit of Hawaiian thing occuring here so you can play around with that or not.

History section would be a nice add as well.
Such as a history section of the Brackenridge itself.

```html
<!DOCTYPE html>
<html lang="en">
<head>
<meta charset="utf-8">
<title>Brackenridge Fish House Menu</title>
<link href="https://fonts.googleapis.com/css2?family=Alfa+Slab+One&family=Arimo:wght@400;700&display=swap" rel="stylesheet">
<style>
:root{
  --page:#ffffff;
  --lavender:#7c83b4;
  --lavender-light:#f4f4f8;
  --bar:#a9a9ab;
  --bar-edge:#6e6e72;
  --gold:#f6c21a;
  --ink:#1c1c22;
  --yellow:#fcbf12;
  --slate:#67667c;
  --olive:#8a9f5a;
  --taupe:#9b8566;
  --stone:#a39c9d;
  --logo-blue:#1d5ea8;
}
*{box-sizing:border-box;margin:0;padding:0}
html,body{width:1200px;height:900px;overflow:hidden;background:var(--page)}
body{position:relative;font-family:"Arimo",Arial,sans-serif;color:var(--ink)}
.sheet{position:absolute;box-shadow:3px 4px 8px rgba(0,0,0,.45)}
.sheet--food{left:50px;top:40px;width:550px;height:430px;z-index:2;
  background:radial-gradient(ellipse 60% 62% at 52% 50%,var(--lavender-light) 0%,#dedfea 45%,var(--lavender) 100%)}
.sheet--wine{left:555px;top:365px;width:565px;height:445px;z-index:1;background:var(--yellow);overflow:hidden}
.section-bar{position:absolute;height:15px;background:var(--bar);border:1px solid var(--bar-edge);border-radius:4px;
  font-family:"Alfa Slab One",serif;font-size:9px;letter-spacing:.5px;color:var(--gold);text-align:center;line-height:13px;
  -webkit-text-stroke:.3px #7a5a00}
.menu-list{position:absolute;list-style:none;font-size:6.4px;line-height:10px}
.menu-list li.sub{padding-left:12px}
.menu-list li.sub::before{content:"•";margin-right:5px}
.menu-list .num{display:inline-block;width:11px;text-align:right;margin-right:5px}
.menu-list li.wrap{padding-left:16px}
.art{position:absolute}
.sweets-box{position:absolute;left:372px;top:142px;width:176px;height:67px;background:var(--bar);border:1px solid var(--bar-edge);border-radius:6px}
.brand{position:absolute;display:flex;align-items:center;justify-content:center;gap:3px;
  font-size:7px;font-weight:700;color:var(--logo-blue);background:#fff;border-radius:50%}
.brand .dot{width:5px;height:5px;background:var(--logo-blue);border-radius:50%}
.tagline{position:absolute;left:455px;top:134px;font-size:8px;font-weight:700;color:#fff}
.family{position:absolute;left:230px;top:386px;font-size:6.5px}
</style>
</head>
<body>

<section class="sheet sheet--food">
  <div class="art" style="left:50px;top:15px;width:70px;height:70px;border-radius:50%;background:radial-gradient(circle,#58a84a,#1f3d24)" role="img" aria-label="Salad bowl with vegetables illustration"></div>

  <div class="section-bar" style="left:8px;top:97px;width:177px">SMALL PLATES</div>
  <ol class="menu-list" style="left:4px;top:120px">
    <li><span class="num">1.</span>Sweet Thai Chili Calamari</li>
    <li><span class="num">2.</span>Shrimp Stuffed Jalapeños</li>
    <li><span class="num">3.</span>Hamachi Crudo</li>
    <li><span class="num">4.</span>House Smoked Salmon with Tandem</li>
    <li class="wrap">Crackers and Pickled Celery</li>
    <li><span class="num">5.</span>Seared Teriyaki Tidbits</li>
    <li><span class="num">6.</span>Sliders</li>
    <li class="sub" style="padding-left:22px">Crab Salad</li>
    <li class="sub" style="padding-left:22px">Sausage with Caramelized Onions, Peppers and</li>
    <li class="wrap" style="padding-left:30px">Provolone</li>
    <li><span class="num">7.</span>Mini Cheeseburgers</li>
    <li><span class="num">8.</span>Fried Green Tomatoes with Crab and Tarragon-Chive</li>
    <li class="wrap">Aioli</li>
    <li><span class="num">9.</span>Tomato Soup</li>
    <li><span class="num">10.</span>Seafood Bisque</li>
    <li><span class="num">11.</span>House Salad with Choice of Dressings</li>
    <li><span class="num">12.</span>Small Caesar Salad</li>
  </ol>

  <div class="section-bar" style="left:12px;top:302px;width:175px">FARM</div>
  <ol class="menu-list" style="left:4px;top:324px">
    <li><span class="num">13.</span>Caesar Salad Entrees</li>
    <li class="sub" style="padding-left:26px">Chicken</li>
    <li class="sub" style="padding-left:26px">Fish</li>
    <li class="sub" style="padding-left:26px">Crab</li>
    <li><span class="num">14.</span>Seafood Cobb</li>
    <li><span class="num">15.</span>Caprese</li>
    <li><span class="num">16.</span>Farmhouse</li>
  </ol>
  <div class="art" style="left:105px;top:325px;width:115px;height:95px;border-radius:4px;background:linear-gradient(160deg,#8a8aa8,#c9b28f)" role="img" aria-label="Person fishing from a rock illustration"></div>

  <div class="section-bar" style="left:188px;top:10px;width:172px">SNACKS</div>
  <ol class="menu-list" style="left:180px;top:32px">
    <li><span class="num">17.</span>Fish Tacos</li>
    <li><span class="num">18.</span>Rolls</li>
    <li><span class="num">19.</span>Lobster</li>
    <li><span class="num">20.</span>Crab</li>
    <li><span class="num">21.</span>Shrimp</li>
    <li><span class="num">22.</span>Grilled Chicken Avocado and Bacon</li>
    <li><span class="num">23.</span>Grilled Cheese with Tomato Soup</li>
  </ol>
  <div class="art" style="left:230px;top:118px;width:100px;height:72px;border-radius:45%;background:radial-gradient(circle,#d9372e,#8e1d18)" role="img" aria-label="Red crab illustration"></div>

  <div class="section-bar" style="left:192px;top:203px;width:173px">OCEANS</div>
  <ol class="menu-list" style="left:180px;top:226px">
    <li><span class="num">24.</span>Wood Grilled Black Smoked Sea Salt and Pepper</li>
    <li class="wrap" style="padding-left:30px">Salmon</li>
    <li><span class="num">25.</span>Miso Black Cod</li>
    <li><span class="num">26.</span>Vela Rino White Fish</li>
    <li><span class="num">27.</span>Whole Fish</li>
    <li><span class="num">28.</span>Fish n Chips</li>
    <li><span class="num">29.</span>Lobster</li>
    <li><span class="num">30.</span>Steamed Clams and/or Mussels</li>
    <li><span class="num">31.</span>Seared Scallops</li>
    <li><span class="num">32.</span>Roasted Garlic Shrimp</li>
    <li><span class="num">33.</span>Crab Cakes with Trio of Dipping Butters</li>
  </ol>
  <div class="art" style="left:310px;top:295px;width:110px;height:90px;border-radius:40%;background:radial-gradient(circle,#6b8a5a,#c3332a)" role="img" aria-label="Cyclist riding a bike with tomato wheels illustration"></div>

  <div class="art" style="left:420px;top:20px;width:80px;height:50px;border-radius:6px;background:linear-gradient(135deg,#e2622b,#8a2a22)" role="img" aria-label="Cut of steak illustration"></div>

  <div class="section-bar" style="left:372px;top:76px;width:176px">RANCH</div>
  <ol class="menu-list" style="left:364px;top:98px">
    <li><span class="num">34.</span>Wood Grilled 16 oz Rib Eye</li>
    <li><span class="num">35.</span>Wood Grilled 10 oz Top Sirloin</li>
    <li><span class="num">36.</span>Wood Grilled Half Chicken</li>
    <li><span class="num">37.</span>Wood Grilled Pork Chop</li>
  </ol>

  <div class="sweets-box"></div>
  <div class="section-bar" style="left:374px;top:145px;width:172px">SWEETS</div>
  <ol class="menu-list" style="left:366px;top:169px">
    <li><span class="num">38.</span>Key Lime Pie</li>
    <li><span class="num">39.</span>Molted Chocolate Cake</li>
    <li><span class="num">40.</span>Banana Fosters / Cherries Jubilee</li>
  </ol>
  <div class="art" style="left:418px;top:220px;width:92px;height:72px;border-radius:50%;background:radial-gradient(circle,#b5d65a,#4a8fd0)" role="img" aria-label="Key lime pie on a plate illustration"></div>

  <div class="brand" style="left:474px;top:372px;width:78px;height:44px;border:1.5px solid var(--logo-blue)"><span class="dot"></span>Brackenridge</div>
</section>

<section class="sheet sheet--wine">
  <div class="section-bar" style="left:0;top:28px;width:190px">WINES</div>
  <ol class="menu-list" style="left:4px;top:52px">
    <li><span class="num">1.</span>Sweet Thai Chili Calamari</li>
    <li><span class="num">2.</span>Shrimp Stuffed Jalapeños</li>
    <li><span class="num">3.</span>Hamachi Crudo</li>
    <li><span class="num">4.</span>House Smoked Salmon with Tandem</li>
    <li class="wrap">Crackers and Pickled Celery</li>
    <li><span class="num">5.</span>Seared Teriyaki Tidbits</li>
    <li><span class="num">6.</span>Sliders</li>
    <li class="sub" style="padding-left:22px">Crab Salad</li>
    <li class="sub" style="padding-left:22px">Sausage with Caramelized Onions, Peppers and</li>
    <li class="wrap" style="padding-left:30px">Provolone</li>
    <li><span class="num">7.</span>Mini Cheeseburgers</li>
    <li><span class="num">8.</span>Fried Green Tomatoes with Crab and Tarragon-Chive</li>
    <li class="wrap">Aioli</li>
    <li><span class="num">9.</span>Tomato Soup</li>
    <li><span class="num">10.</span>Seafood Bisque</li>
    <li><span class="num">11.</span>House Salad with Choice of Dressings</li>
    <li><span class="num">12.</span>Small Caesar Salad</li>
  </ol>
  <ol class="menu-list" style="left:4px;top:268px">
    <li><span class="num">13.</span>Caesar Salad Entrees</li>
    <li class="sub" style="padding-left:26px">Chicken</li>
    <li class="sub" style="padding-left:26px">Fish</li>
    <li class="sub" style="padding-left:26px">Crab</li>
    <li><span class="num">14.</span>Seafood Cobb</li>
    <li><span class="num">15.</span>Caprese</li>
    <li><span class="num">16.</span>Farmhouse</li>
  </ol>

  <div class="art" style="left:200px;top:265px;width:158px;height:92px;border-radius:4px;background:linear-gradient(90deg,#b8323a 0%,#e9e2e2 45%,#e9e2e2 55%,#d22b2b 100%)" role="img" aria-label="Crossed American and Canadian flags illustration"></div>
  <p class="family">Family Owned and Operated</p>

  <div class="art" style="left:363px;top:0;width:202px;height:445px;background:linear-gradient(180deg,var(--slate) 0 18%,transparent 18%),linear-gradient(90deg,var(--olive) 0 38%,var(--yellow) 38% 62%,var(--taupe) 62%);" role="img" aria-label="Restaurant wall and floor backdrop with wine bottle, grapes, vegetables and roast chicken illustrations"></div>
  <div class="art" style="left:363px;top:335px;width:202px;height:110px;background:var(--stone)" aria-hidden="true"></div>
  <div class="art" style="left:430px;top:52px;width:66px;height:40px;border-radius:50%;background:radial-gradient(circle,#f49a2a,#fff 80%)" role="img" aria-label="Fish illustration in a circle"></div>
  <div class="art" style="left:396px;top:307px;width:32px;height:135px;border-radius:10px 10px 2px 2px;background:linear-gradient(90deg,#5a1a1c,#a0323a)" role="img" aria-label="Red wine bottle illustration"></div>
  <p class="tagline">"Eat the Fish"</p>
  <div class="brand" style="left:423px;top:182px;width:80px;height:42px;border:1.5px solid var(--logo-blue)"><span class="dot"></span>Brackenridge</div>
</section>

</body>
</html>
```